L' Vela Breeze, 95% quality oxygen

Task description
L' Vela Breeze, is quality oxygen can for everyone. Our target countries are USA and Europe. Those who exhausted from intense exercises, stress from work, hangover from drinking, or ever those caused by altitude. Therefore, the concept of label must be freshening up after use with elegance and luxury look.
Our can size is as follow.
Diameter: 3.8 cm
Height: 12.8 cm
Requirement of label.
- Width: 12.5 cm
- Height: 11 cm
- Vela Breeze and Logo must not be changed. (W 3.5 cm x H 3 cm)
- Font: All detail must be black color. But each heading section such as Tips, Easy steps for use, Caution must be highlighted or in other notable color.
- The layout of label is flexible. However, we want Vela Breeze and logo on top of the can.
- Leave a little space below L' Vela Breeze logo then put “Jasmine Rose scent” with gold color highlighted
- Follow by “95% quality oxygen” and “Up to 45+ inhalations”
- At the bottom of bottle must be “4 liters of oxygen”
- Please design 4 vectors to put on the label. We need running or cardio exercise, drinking, recovery, altitude. The vectors given are samples only.
- We expected to have snowflake as theme color (glossy white) on label background. It could be falling snowflake, thick layer of snow on the ground, snow on mountains.
- Please leave some space for barcode.
Target Market(s)
Our target countries are USA and Europe. Those who exhausted from intense exercises, stress from work, hangover from drinking, or ever those caused by altitude.
Requirements
Must have
- Requirement of label.
- - Width: 12.5 cm
- - Height: 11 cm
- - Vela Breeze and Logo must not be changed. (W 3.5 cm x H 3 cm)
- - Font: All detail must be black color. But each heading section such as Tips, Easy steps for use, Caution must be highlighted or in other notable color.
- - The layout of label is flexible. However, we want L' Vela Breeze and logo on top of the can.
- - Leave a little space below L' Vela Breeze logo then put “Jasmine Rose scent” with gold color highlighted
- - Follow by “95% quality oxygen” and “Up to 45+ inhalations”
- - At the bottom of bottle must be “4 liters of oxygen”
- - Please design 4 vectors to put on the label. We need running or cardio exercise, drinking, recovery, altitude. The vectors given are samples only.
- - We expected to have snowflake as theme color (white) on label background. It could be falling snowflake, thick layer of snow on the ground, snow on mountains.
- - Please leave some space for barcode.
Nice to have
- We want our product to be very notable, classy, international, luxury look with glossy white color and clean+anti-fingerprints. Easy to read even though the font size is small.
Should not have
- cartoon design, not classy or luxury.

```html
<!DOCTYPE html>
<html lang="en">
<head>
<meta charset="utf-8">
<title>L' Vela Breeze – Oxygen Can Label</title>
<link rel="stylesheet" href="https://fonts.googleapis.com/css2?family=Montserrat:wght@500;600;700&family=Open+Sans:wght@400;600;700&display=swap">
<style>
  :root {
    --stage-top: #f4f4f4;
    --stage-bottom: #8e8e8e;
    --label-light: #f3f4f6;
    --label-mid: #d9dbde;
    --label-edge: #b9bcc1;
    --frost: #c9d8ea;
    --frost-soft: #e4ecf5;
    --ink: #111111;
    --gold: #9a7422;
    --gold-light: #c39a3c;
    --frame: #9fb6d3;
    --white: #ffffff;
  }
  * { box-sizing: border-box; margin: 0; padding: 0; }
  html, body { width: 1200px; height: 1000px; overflow: hidden; }
  body {
    background: linear-gradient(180deg, var(--stage-top) 0%, #dcdcdc 45%, var(--stage-bottom) 100%);
    font-family: "Open Sans", Arial, sans-serif;
    color: var(--ink);
    position: relative;
  }
  .label {
    position: absolute;
    top: 190px;
    width: 340px;
    height: 620px;
    background: linear-gradient(90deg, var(--label-edge) 0%, var(--label-light) 30%, var(--white) 50%, var(--label-mid) 80%, var(--label-edge) 100%);
    box-shadow: 0 10px 30px rgba(0,0,0,0.18);
    overflow: hidden;
  }
  .label--front { left: 230px; }
  .label--back { left: 630px; }

  .snow-pattern {
    position: absolute;
    inset: 0;
    background:
      radial-gradient(circle at 12% 22%, var(--frost) 0 26px, transparent 48px),
      radial-gradient(circle at 85% 8%, var(--frost) 0 30px, transparent 54px),
      radial-gradient(circle at 92% 50%, var(--frost-soft) 0 22px, transparent 44px),
      radial-gradient(circle at 8% 78%, var(--frost) 0 24px, transparent 46px),
      radial-gradient(circle at 88% 86%, var(--frost) 0 28px, transparent 50px);
    opacity: 0.7;
  }

  /* Front */
  .front-content {
    position: relative;
    height: 100%;
    display: flex;
    flex-direction: column;
    align-items: center;
    text-align: center;
  }
  .brand {
    margin-top: 110px;
    display: flex;
    flex-direction: column;
    align-items: center;
    gap: 14px;
  }
  .brand__dot {
    width: 54px; height: 54px;
    border-radius: 50%;
    background: var(--ink);
  }
  .brand__name {
    font-family: "Montserrat", Arial, sans-serif;
    font-weight: 600;
    font-size: 30px;
    letter-spacing: 1px;
    color: var(--ink);
    line-height: 1;
  }
  .scent-band {
    margin-top: 36px;
    background: linear-gradient(90deg, var(--gold) 0%, var(--gold-light) 50%, var(--gold) 100%);
    color: var(--white);
    font-family: "Montserrat", Arial, sans-serif;
    font-weight: 600;
    font-size: 13px;
    letter-spacing: 1.5px;
    padding: 5px 18px;
    border: 2px solid #5f4512;
  }
  .stat {
    font-family: "Montserrat", Arial, sans-serif;
    font-weight: 700;
    letter-spacing: 1px;
    line-height: 1.35;
  }
  .stat--purity { margin-top: 70px; font-size: 12px; }
  .stat--purity .stat__big { font-size: 17px; }
  .stat--inhale { margin-top: 34px; font-size: 12px; }
  .stat--inhale .stat__big { font-size: 17px; }
  .stat--volume { margin-top: auto; margin-bottom: 52px; font-size: 12px; }
  .stat--volume .stat__big { font-size: 17px; }

  /* Back */
  .back-content {
    position: relative;
    padding: 26px 22px 0 22px;
    display: flex;
    flex-direction: column;
  }
  .back-brand {
    display: flex;
    align-items: center;
    justify-content: center;
    gap: 10px;
    margin-bottom: 18px;
  }
  .back-brand__dot {
    width: 28px; height: 28px; border-radius: 50%; background: var(--ink);
  }
  .back-brand__name {
    font-family: "Montserrat", Arial, sans-serif;
    font-weight: 600;
    font-size: 19px;
    letter-spacing: 0.5px;
  }
  .info-block {
    border: 1px solid var(--frame);
    margin-bottom: 4px;
    padding-bottom: 6px;
  }
  .info-block__heading {
    display: inline-block;
    background: linear-gradient(90deg, var(--gold) 0%, var(--gold-light) 100%);
    color: var(--white);
    font-family: "Montserrat", Arial, sans-serif;
    font-weight: 700;
    font-size: 11px;
    letter-spacing: 1.5px;
    padding: 2px 10px;
    margin-bottom: 6px;
  }
  .info-block__list { list-style: none; padding: 0 10px; }
  .info-block__list li {
    position: relative;
    padding-left: 14px;
    font-size: 9.5px;
    font-weight: 600;
    line-height: 1.35;
    margin-bottom: 5px;
  }
  .info-block__list li::before {
    content: "";
    position: absolute;
    left: 0; top: 3px;
    width: 6px; height: 6px;
    background: var(--gold);
  }
  .uses {
    display: flex;
    justify-content: space-around;
    margin-top: 12px;
  }
  .use {
    display: flex;
    flex-direction: column;
    align-items: center;
    gap: 5px;
    width: 60px;
  }
  .use__icon {
    width: 26px; height: 30px;
    background: var(--ink);
    border-radius: 4px;
  }
  .use__label {
    font-size: 6.5px;
    font-weight: 700;
    letter-spacing: 0.5px;
    text-align: center;
    line-height: 1.2;
  }
  .disclaimer {
    margin-top: 10px;
    font-size: 9px;
    font-weight: 700;
    text-align: center;
    line-height: 1.35;
  }
  .origin {
    margin-top: 8px;
    font-size: 7px;
    font-weight: 600;
    text-align: center;
  }
  .website {
    margin-top: 8px;
    font-family: "Montserrat", Arial, sans-serif;
    font-weight: 700;
    font-size: 11px;
    letter-spacing: 1px;
    text-align: center;
  }
  .barcode-space { height: 46px; margin-top: 8px; }
</style>
</head>
<body>

  <section class="label label--front">
    <div class="snow-pattern" role="img" aria-label="Soft falling snowflake pattern in pale icy blue"></div>
    <div class="front-content">
      <div class="brand">
        <span class="brand__dot"></span>
        <span class="brand__name">L' VELA BREEZE</span>
      </div>
      <div class="scent-band">JASMINE ROSE SCENT</div>
      <p class="stat stat--purity"><span class="stat__big">95%</span><br>QUALITY OXYGEN</p>
      <p class="stat stat--inhale">UP TO <span class="stat__big">45+</span><br>INHALATIONS</p>
      <p class="stat stat--volume"><span class="stat__big">4</span> LITERS<br>OF OXYGEN</p>
    </div>
  </section>

  <section class="label label--back">
    <div class="snow-pattern" role="img" aria-label="Soft falling snowflake pattern in pale icy blue"></div>
    <div class="back-content">
      <div class="back-brand">
        <span class="back-brand__dot"></span>
        <span class="back-brand__name">L' VELA BREEZE</span>
      </div>

      <div class="info-block">
        <span class="info-block__heading">TIPS</span>
        <ul class="info-block__list">
          <li>Our quality oxygen is best to use when exhausted from intense exercises, stressful work, or even hangover from a long night party. Deeply breathing our quality oxygen for 2 seconds per shot and repeat up to 5 times.</li>
          <li>Over breathing than suggestion would cause dizziness.</li>
        </ul>
      </div>

      <div class="info-block">
        <span class="info-block__heading">EASY STEPS FOR USE:</span>
        <ul class="info-block__list">
          <li>Open the lid.</li>
          <li>Place the cap close to mouth.</li>
          <li>Press the cap to activate quality oxygen and inhale simultaneously.</li>
        </ul>
      </div>

      <div class="info-block">
        <span class="info-block__heading">CAUTION:</span>
        <ul class="info-block__list">
          <li>Non-flammable.</li>
          <li>Pressurizing container, store at temperature less than 50 °C</li>
          <li>Do not pierce or burn even empty.</li>
        </ul>
      </div>

      <div class="uses">
        <div class="use"><span class="use__icon" role="img" aria-label="Pictogram of a runner for cardio exercises"></span><span class="use__label">CARDIO<br>EXERCISES</span></div>
        <div class="use"><span class="use__icon" role="img" aria-label="Pictogram of a person drinking"></span><span class="use__label">DRINKING</span></div>
        <div class="use"><span class="use__icon" role="img" aria-label="Pictogram of a person recovering at rest"></span><span class="use__label">RECOVERY</span></div>
        <div class="use"><span class="use__icon" role="img" aria-label="Pictogram of a hiker climbing at altitude"></span><span class="use__label">ALTITUDE</span></div>
      </div>

      <p class="disclaimer">This product is not certified by FDA. The purpose is not for curing or preventing any symptoms.</p>
      <p class="origin">Made in Thailand</p>
      <p class="website">www.velabreeze-air.com</p>
      <div class="barcode-space"></div>
    </div>
  </section>

</body>
</html>
```